Label Design for Amber Reed Specialty Coffee Roasters

We are a specialty coffee beans Roasting Shop named "Amber Reed". We pack our beans in stand up poaches of varying sizes. We sell beans both to B2C and B2B and are looking to design stickers that will stand out. Our logo was designed with a black and white background. So far, we have been using white glossy bean bags and came up with a front label design that we would like to use for our labels.
We would like to see the design tweaked to fit both a white bag and a black one.
Currently, the attached front label design does not work on white bags. We would also like to have a back sticker designed that needs to include: 1- a description section for the type of beans used 2- a QR code section

Target Market(s)

Specialty beans in our area are typically liked by the younger generations 40 years and younger. Both male and females drink our coffee with varying income levels. But generally, middle class and above buy our coffee beans.

Requirements
Must have
• We are am looking for a sticker to be placed on a coffee bean bag. The sticker needs to contain the roasting shop's logo and brand name "Amber Reed". Also, the sticker needs to have the following: country name, bean variety, weight (kg), roast date. The sticker needs to have the following specifications on a 5 point Likert scale (Strength, Fruitiness, Earthiness, Brightness). I uploaded a front label design that needs to be tweaked to fit both a white bag and a black one. The current design has owls representing the 5 point Likert scale and part of the shop's logo. We would like to keep that part of the design if possible. Currently, the attached front label design does not work on white bags.
We would also like to have a back sticker designed that needs to include: 1- a description section for the type of beans used 2- a QR code section
Nice to have
• The font that is used in the logo is League Gothic. It is okay to use this font or any other font if you find it more appropriate for the design.

```html
<!DOCTYPE html>
<html lang="en">
<head>
<meta charset="utf-8">
<title>Amber Reed Specialty Coffee Roasters – Front Label</title>
<link href="https://fonts.googleapis.com/css2?family=League+Gothic&display=swap" rel="stylesheet">
<style>
  :root {
    --page-bg: #e4e9ec;
    --label-bg: #ffffff;
    --ink: #111111;
    --muted-ink: #b5b5b5;
    --rule: #1a1a1a;
  }
  * { margin: 0; padding: 0; box-sizing: border-box; }
  html, body {
    width: 1200px;
    height: 845px;
    overflow: hidden;
    background: var(--page-bg);
  }
  .canvas {
    position: relative;
    width: 1200px;
    height: 845px;
  }
  .label {
    position: absolute;
    left: 300px;
    top: 28px;
    width: 600px;
    height: 788px;
    background: var(--label-bg);
    color: var(--ink);
    font-family: "League Gothic", "Arial Narrow", sans-serif;
    box-shadow: 0 4px 14px rgba(0, 0, 0, 0.18);
  }
  .label__quote {
    position: absolute;
    left: 0;
    top: 0;
    width: 600px;
    height: 320px;
  }
  .label__quote text {
    font-family: "League Gothic", "Arial Narrow", sans-serif;
    font-size: 31px;
    fill: var(--ink);
    letter-spacing: 0.5px;
  }
  .brand-name {
    position: absolute;
    left: 0;
    top: 250px;
    width: 600px;
    text-align: center;
    font-size: 82px;
    line-height: 1;
    letter-spacing: 1px;
    color: var(--ink);
  }
  .rule {
    position: absolute;
    left: 36px;
    width: 528px;
    height: 2px;
    background: var(--rule);
  }
  .rule--v {
    width: 2px;
    height: auto;
  }
  .origin-row {
    position: absolute;
    top: 433px;
    height: 58px;
    display: flex;
    align-items: center;
    justify-content: center;
    font-size: 37px;
    letter-spacing: 0.5px;
  }
  .origin-row--country { left: 36px; width: 285px; }
  .origin-row--bean { left: 321px; width: 243px; }
  .profile {
    position: absolute;
    left: 48px;
    top: 506px;
    width: 390px;
    list-style: none;
  }
  .profile__row {
    display: flex;
    align-items: center;
    height: 50px;
  }
  .profile__name {
    width: 192px;
    font-size: 37px;
    letter-spacing: 0.5px;
  }
  .profile__scale {
    display: flex;
    gap: 16px;
  }
  .cup {
    width: 32px;
    height: 30px;
    color: var(--ink);
  }
  .cup--empty { color: var(--muted-ink); }
  .weight {
    position: absolute;
    left: 448px;
    top: 552px;
    width: 116px;
    text-align: center;
    font-size: 37px;
    line-height: 1.05;
    letter-spacing: 0.5px;
  }
  .weight__value {
    display: block;
    font-size: 33px;
  }
  .roast-date {
    position: absolute;
    left: 48px;
    top: 715px;
    font-size: 37px;
    letter-spacing: 0.5px;
  }
</style>
</head>
<body>
<svg width="0" height="0" style="position:absolute" aria-hidden="true">
  <symbol id="icon-cup" viewBox="0 0 32 30">
    <path d="M15 2c-2 2 2 3 0 6M18 3c-1.5 1.5 1.5 2.5 0 5" fill="none" stroke="currentColor" stroke-width="1.4" stroke-linecap="round"/>
    <path d="M6 11h19v5c0 5-4 8-9.5 8S6 21 6 16z" fill="currentColor"/>
    <path d="M25 13c4 0 4 5 0 5" fill="none" stroke="currentColor" stroke-width="2"/>
    <ellipse cx="15.5" cy="26" rx="13" ry="3" fill="currentColor"/>
  </symbol>
</svg>

<main class="canvas">
  <article class="label" aria-label="Amber Reed front coffee label">
    <svg class="label__quote" viewBox="0 0 600 320" aria-hidden="false">
      <defs>
        <path id="quote-arc" d="M 30 302 A 270 270 0 0 1 570 302"/>
      </defs>
      <text>
        <textPath href="#quote-arc" startOffset="50%" text-anchor="middle" textLength="760" lengthAdjust="spacing">I DON´T NEED AN INSPIRATIONAL QUOTE. I NEED COFFEE</textPath>
      </text>
    </svg>

    <h1 class="brand-name">AMBER REED</h1>

    <div class="rule" style="top:433px"></div>
    <div class="origin-row origin-row--country">COLOMBIA VARIETY</div>
    <div class="rule rule--v" style="left:320px; top:433px; height:58px"></div>
    <div class="origin-row origin-row--bean">100%ARABIC</div>
    <div class="rule" style="top:490px"></div>

    <ul class="profile">
      <li class="profile__row">
        <span class="profile__name">STRENGHT</span>
        <span class="profile__scale" aria-label="2 of 5">
          <svg class="cup"><use href="#icon-cup"/></svg>
          <svg class="cup"><use href="#icon-cup"/></svg>
          <svg class="cup cup--empty"><use href="#icon-cup"/></svg>
          <svg class="cup cup--empty"><use href="#icon-cup"/></svg>
          <svg class="cup cup--empty"><use href="#icon-cup"/></svg>
        </span>
      </li>
      <li class="profile__row">
        <span class="profile__name">FRUITNESS</span>
        <span class="profile__scale" aria-label="3 of 5">
          <svg class="cup"><use href="#icon-cup"/></svg>
          <svg class="cup"><use href="#icon-cup"/></svg>
          <svg class="cup"><use href="#icon-cup"/></svg>
          <svg class="cup cup--empty"><use href="#icon-cup"/></svg>
          <svg class="cup cup--empty"><use href="#icon-cup"/></svg>
        </span>
      </li>
      <li class="profile__row">
        <span class="profile__name">EARTHINESS</span>
        <span class="profile__scale" aria-label="3 of 5">
          <svg class="cup"><use href="#icon-cup"/></svg>
          <svg class="cup"><use href="#icon-cup"/></svg>
          <svg class="cup"><use href="#icon-cup"/></svg>
          <svg class="cup cup--empty"><use href="#icon-cup"/></svg>
          <svg class="cup cup--empty"><use href="#icon-cup"/></svg>
        </span>
      </li>
      <li class="profile__row">
        <span class="profile__name">BRIGHTNESS</span>
        <span class="profile__scale" aria-label="2 of 5">
          <svg class="cup"><use href="#icon-cup"/></svg>
          <svg class="cup"><use href="#icon-cup"/></svg>
          <svg class="cup cup--empty"><use href="#icon-cup"/></svg>
          <svg class="cup cup--empty"><use href="#icon-cup"/></svg>
          <svg class="cup cup--empty"><use href="#icon-cup"/></svg>
        </span>
      </li>
    </ul>

    <div class="rule rule--v" style="left:446px; top:490px; height:218px"></div>
    <div class="weight">WEIGHT<span class="weight__value">250g</span></div>

    <div class="rule" style="top:707px"></div>
    <div class="roast-date">ROAST DATE:</div>
    <div class="rule" style="top:762px"></div>
  </article>
</main>
</body>
</html>
```